Premium Photoshop/Illustrator Template for Adventure Map Prints

Premium Adventure Print Template for KELVO Adventure
About the Project
I am launching a business called KELVO Adventure.
Customers send me a GPS track (GPX file) from an adventure they have completed, such as:
Trail running
Hiking
Mountain biking
Ski touring
Road cycling
Mountain ascents
Adventure racing
I create a high-quality map using professional GIS software and produce a premium wall print that commemorates their adventure.
This is not a one-off poster design.
I need a reusable Photoshop template that I can use for hundreds of different adventures by simply replacing the map, statistics and adventure information.
Design Style
I am looking for a design that feels:
Premium
Modern
Minimal
Clean
Sophisticated
Timeless
The finished product should look like something people would proudly frame and display in their home.
I like the clean, premium aesthetic of brands such as Torvik, VANTU, Milvok, Pelora and BluMesa.
I prefer subtle, elegant design rather than something busy or cluttered.
The map should always be the hero of the design.
This should feel like premium wall art rather than a dashboard of statistics. The information should enhance the story of the adventure without competing with the map for attention.
Template Requirements
The Photoshop template should include editable placeholders for:
Adventure title
Athlete name
Date
Main map
Adventure statistics
Elevation profile
Optional race or event photo
Optional event logo
KELVO Adventure logo
Website address
Optional location icon or subtle design elements
The map and elevation profile will be created by me using professional GIS software and inserted into the template.
The designer does not need to create these graphics.
Layout Preference
My preferred direction is for the map to extend to the edges of the print wherever possible, with the information presented as subtle floating panels over the map rather than within a large fixed sidebar.
The map should occupy as much of the page as possible and remain the primary visual focus.
The main information panel should be compact and elegant, allowing the artwork to dominate the composition rather than the information.
The layout should feel balanced, modern and premium while remaining practical to update for hundreds of different adventures.
Flexibility
The template needs to work with adventures of many different shapes and sizes.
Some routes are short loops.
Others may be over 100 km long.
The layout should work equally well in both portrait and landscape orientations and should scale naturally from A3 through to A0 without requiring the design to be recreated.
The template should also work equally well for trail running, hiking, mountain biking, road cycling, ski touring and other adventure sports.
Modular Layout
This template will become a reusable design system rather than a single fixed poster layout.
I would like the template to consist of several logical grouped elements that can easily be updated for each new adventure.
Main Information Panel
The following elements should form one grouped panel:
Adventure title
Athlete name
Date
Adventure statistics
Optional Torvik-inspired metric dial
KELVO Adventure logo
Website address
This grouped panel should be easy to resize and reposition if required so that it works with different map layouts, route shapes and print sizes.
The information panel should remain subtle and elegant. It should support the map rather than dominate it.
The KELVO Adventure logo should be used as discreet branding rather than the main visual focus.
Typical statistics may include:
Distance
Elevation gain
Moving time
Average pace or average speed
Maximum elevation
Date
Additional metrics may be displayed depending on the activity.
Elevation Profile
The elevation profile should be a separate replaceable placeholder that can easily be updated for each new adventure without recreating the design.
It should also be able to be repositioned or resized if required to best suit the overall composition.
Optional Photo / Event Panel
Please include a separate optional placeholder for a race photo, event logo or similar content.
This element should be able to be shown or hidden while the overall layout still feels balanced and intentional.
Speed/Pace Legend
Please include an optional placeholder for the route colour legend. This should be designed as a separate element that can be shown, hidden or repositioned depending on the adventure while maintaining a clean, balanced layout.
Deliverables
Please supply:
Fully layered Photoshop (.PSD) files
Landscape template (A3)
Portrait template (A3)
Both templates should use the same design language and branding
Clearly organised layer groups
Editable text layers
Smart Objects or an equally simple method for replacing the map, elevation profile and optional images
Locked design elements where appropriate
Print-ready at 300 dpi
The templates should be quick and intuitive to update for each new adventure.
The templates should also be designed so they can be easily adapted to A2, A1 and A0 print sizes without requiring the layout to be redesigned.
Source Files
Please provide:
Layered Photoshop (.PSD) files
Any Illustrator (.AI) files used during the design process
Names of all fonts used (preferably Adobe Fonts where possible)
Any graphics or assets used within the design
Files Provided
I have attached:
My current draft design
The KELVO Adventure logo
Sample map artwork
A Torvik watch face for design inspiration
These are intended to demonstrate the concept only.
I am looking for a designer to create a much more polished, modern and premium version of this product.
Creative Direction
Please don't feel constrained by my existing layout. The attached design is simply to demonstrate the concept and the information that needs to be included.
I welcome fresh, creative ideas and different layouts, provided the design remains clean, premium and the map remains the hero of the print.
I particularly like the clean design language and circular metric dial shown on the Torvik watch face. I would like this to be explored as an optional design element, but not copied directly.
I also like the idea of incorporating a very subtle contour or topographic line texture into the information panels or backgrounds to reinforce the outdoor and mapping theme. This should remain understated and elegant so it adds depth without distracting from the map.
The finished template should establish a distinctive visual identity that can be used consistently across the KELVO Adventure product range.
When someone receives one of these prints, I want their first reaction to be "Wow." It should celebrate the adventure, tell the story of the journey and become something they are proud to frame and display in their home.
Update - I have attached a couple of files that I would like to explore incorporating into the background of my information boxes, maybe just a subtle contour texture, similar to the watch face attached.
Workflow clarification: This template will be used to produce many posters. For each order, I'll be replacing the map, GPX route and statistics with new content exported from QGIS. My priority is an efficient workflow that allows me to update these elements quickly while maintaining a high-quality design. I'm happy for the master template to be created in Illustrator if that's the best approach, with Photoshop used where appropriate for image editing. Please keep this workflow in mind when designing the template and let me know if you have any recommendations.

```html
<!DOCTYPE html>
<html lang="en">
<head>
<meta charset="utf-8">
<title>KELVO Adventure – Layer Structure</title>
<link href="https://fonts.googleapis.com/css2?family=Roboto:wght@400;500&display=swap" rel="stylesheet">
<style>
  :root{
    --panel:#393939;
    --panel-dark:#2b2b2b;
    --row:#424242;
    --row-line:#303030;
    --row-active:#5e5e5e;
    --field:#2f2f2f;
    --field-line:#5a5a5a;
    --text:#dcdcdc;
    --text-dim:#a9a9a9;
    --icon:#cfcfcf;
    --scroll-track:#333333;
    --scroll-thumb:#5a5a5a;
    --edge:#4a4a4a;
    --map-a:#3c4a3a;
    --map-b:#6f7d64;
    --map-c:#2a3340;
  }
  *{box-sizing:border-box;margin:0;padding:0}
  html,body{width:1200px;height:4349px;overflow:hidden;background:var(--panel-dark)}
  body{position:relative;font-family:"Roboto",Arial,sans-serif;color:var(--text)}

  .map-edge{position:absolute;left:0;top:0;width:65px;height:4349px;
    background:linear-gradient(180deg,var(--map-c) 0%,var(--map-a) 20%,var(--map-b) 45%,var(--map-a) 70%,var(--map-c) 100%)}
  .map-edge__label{position:absolute;left:4px;top:385px;font-size:26px;letter-spacing:2px;color:#f2f2f2;font-weight:500}

  .layers-panel{position:absolute;left:65px;top:0;width:1088px;height:4349px;background:var(--panel)}
  .panel-edge{position:absolute;left:1153px;top:0;width:47px;height:4349px;background:var(--edge)}

  .tab-bar{position:absolute;left:0;top:0;width:1088px;height:146px;background:var(--panel-dark);display:flex;align-items:stretch}
  .tab{display:flex;align-items:center;padding:0 26px;font-size:38px;color:var(--text-dim)}
  .tab--active{background:var(--panel);color:#f0f0f0}
  .tab-bar__more{margin-left:auto;display:flex;align-items:center;gap:40px;padding-right:30px;font-size:38px;color:var(--text-dim)}

  .control-row{position:absolute;left:28px;right:28px;display:flex;align-items:center;gap:26px;font-size:38px}
  .field{height:92px;border:2px solid var(--field-line);background:var(--field);display:flex;align-items:center;justify-content:space-between;padding:0 20px;font-size:38px}
  .filter-icons{display:flex;gap:44px;margin-left:30px;align-items:center}
  .filter-icons svg{width:50px;height:50px}
  .toggle{width:34px;height:60px;border-radius:17px;background:#e8e8e8;margin-left:auto}
  .lock-icons{display:flex;gap:40px;align-items:center}
  .lock-icons svg{width:46px;height:46px}

  .layer-list{position:absolute;left:0;top:498px;width:1037px}
  .layer{position:relative;display:flex;align-items:center;border-bottom:2px solid var(--row-line);background:var(--row)}
  .layer--group{height:96px}
  .layer--item{height:168px}
  .layer--active{background:var(--row-active)}
  .layer__eye{width:144px;height:100%;display:flex;align-items:center;justify-content:center;border-right:2px solid var(--row-line)}
  .layer__eye svg{width:52px;height:34px}
  .layer__chevron{width:30px;height:30px;margin-left:40px}
  .layer__folder{width:64px;height:50px;margin-left:26px}
  .layer__name{font-size:38px;margin-left:30px;white-space:nowrap}
  .layer--root .layer__chevron{margin-left:-16px}
  .layer--child .layer__chevron{margin-left:106px}
  .type-icon{margin-left:166px;font-size:64px;width:60px;text-align:center;color:var(--icon)}
  .layer--text .layer__name{margin-left:56px}
  .thumb{margin-left:98px;width:144px;height:106px;border:2px solid #6b6b6b;
    background:repeating-conic-gradient(#ffffff 0 25%,#cccccc 0 50%) 0 0/24px 24px}
  .thumb--dark{background:linear-gradient(135deg,#1f2a2a,#3e4f47)}
  .thumb--mark{position:relative}
  .thumb--mark::after{content:"";position:absolute;left:10px;bottom:10px;width:44px;height:36px;background:#505a56}
  .thumb--map{background:linear-gradient(135deg,#7c8a6d,#4f5e4c 50%,#9aa38a)}
  .link-icon{width:30px;height:56px;margin-left:12px}
  .mask-thumb{margin-left:12px;width:144px;height:106px;border:2px solid #6b6b6b;background:#6a6a6a;position:relative}
  .mask-thumb::before{content:"";position:absolute;left:0;top:0;width:58px;height:46px;background:#ffffff}
  .layer--item .thumb + .layer__name,.mask-thumb + .layer__name{margin-left:36px}

  .scrollbar{position:absolute;left:1037px;top:498px;width:51px;height:3851px;background:var(--scroll-track)}
  .scrollbar__thumb{position:absolute;left:12px;top:40px;width:27px;height:3500px;border-radius:14px;background:var(--scroll-thumb)}
</style>
</head>
<body>
<svg width="0" height="0" style="position:absolute" aria-hidden="true">
  <symbol id="eye" viewBox="0 0 26 17"><path d="M1 8.5C4 3 8.5 1 13 1s9 2 12 7.5C22 14 17.5 16 13 16S4 14 1 8.5z" fill="none" stroke="#dcdcdc" stroke-width="2"/><circle cx="13" cy="8.5" r="3.6" fill="#dcdcdc"/></symbol>
  <symbol id="chev-down" viewBox="0 0 10 10"><path d="M1 3l4 4 4-4" fill="none" stroke="#cfcfcf" stroke-width="1.4"/></symbol>
  <symbol id="chev-right" viewBox="0 0 10 10"><path d="M3 1l4 4-4 4" fill="none" stroke="#cfcfcf" stroke-width="1.4"/></symbol>
  <symbol id="folder" viewBox="0 0 32 25"><path d="M1 3h11l3 3h16v18H1z" fill="#cfcfcf"/></symbol>
  <symbol id="link" viewBox="0 0 10 20"><rect x="2" y="1" width="6" height="8" rx="3" fill="none" stroke="#cfcfcf" stroke-width="1.5"/><rect x="2" y="11" width="6" height="8" rx="3" fill="none" stroke="#cfcfcf" stroke-width="1.5"/></symbol>
</svg>

<div class="map-edge" role="img" aria-label="Edge of the alpine map artwork with the route print">
  <span class="map-edge__label">OP</span>
</div>

<section class="layers-panel">
  <header class="tab-bar">
    <span class="tab">Colo</span>
    <span class="tab tab--active">Layers</span>
    <span class="tab">Char</span>
    <span class="tab">Path</span>
    <span class="tab">Swat</span>
    <span class="tab-bar__more"><span>»</span><span>≡</span></span>
  </header>

  <div class="control-row" style="top:172px">
    <div class="field" style="width:395px"><span>Kind</span><span>⌄</span></div>
    <div class="filter-icons">
      <svg viewBox="0 0 20 20"><rect x="2" y="3" width="16" height="14" fill="none" stroke="#cfcfcf" stroke-width="2"/><path d="M4 15l5-6 4 4 3-3 2 5z" fill="#cfcfcf"/></svg>
      <svg viewBox="0 0 20 20"><circle cx="10" cy="10" r="8" fill="none" stroke="#cfcfcf" stroke-width="2"/><path d="M10 2a8 8 0 0 1 0 16z" fill="#cfcfcf"/></svg>
      <svg viewBox="0 0 20 20"><path d="M3 3h14v4h-2V5h-4v11h2v2H7v-2h2V5H5v2H3z" fill="#cfcfcf"/></svg>
      <svg viewBox="0 0 20 20"><rect x="4" y="4" width="12" height="12" fill="none" stroke="#cfcfcf" stroke-width="2"/><rect x="2" y="2" width="4" height="4" fill="#cfcfcf"/><rect x="14" y="14" width="4" height="4" fill="#cfcfcf"/></svg>
      <svg viewBox="0 0 20 20"><path d="M4 2h9l3 3v13H4z" fill="none" stroke="#cfcfcf" stroke-width="2"/></svg>
    </div>
    <div class="toggle"></div>
  </div>

  <div class="control-row" style="top:287px">
    <div class="field" style="width:595px"><span>Pass Through</span><span>⌄</span></div>
    <span style="margin-left:20px">Opacity:</span>
    <div class="field" style="width:200px"><span>100%</span><span>⌄</span></div>
  </div>

  <div class="control-row" style="top:394px">
    <span>Lock:</span>
    <div class="lock-icons">
      <svg viewBox="0 0 20 20"><rect x="2" y="2" width="16" height="16" fill="none" stroke="#cfcfcf" stroke-width="2"/><path d="M2 10h16M10 2v16" stroke="#cfcfcf" stroke-width="2"/></svg>
      <svg viewBox="0 0 20 20"><path d="M3 17l3-1 11-11-2-2L4 14z" fill="#cfcfcf"/></svg>
      <svg viewBox="0 0 20 20"><path d="M10 1v18M1 10h18M7 4l3-3 3 3M7 16l3 3 3-3M4 7l-3 3 3 3M16 7l3 3-3 3" fill="none" stroke="#cfcfcf" stroke-width="2"/></svg>
      <svg viewBox="0 0 20 20"><rect x="3" y="3" width="14" height="14" fill="none" stroke="#cfcfcf" stroke-width="2"/></svg>
      <svg viewBox="0 0 20 20"><rect x="4" y="9" width="12" height="9" fill="#cfcfcf"/><path d="M6 9V6a4 4 0 0 1 8 0v3" fill="none" stroke="#cfcfcf" stroke-width="2"/></svg>
    </div>
    <span style="margin-left:auto">Fill:</span>
    <div class="field" style="width:200px"><span>100%</span><span>⌄</span></div>
  </div>

  <div class="layer-list">
    <div class="layer layer--group layer--root"><span class="layer__eye"><svg><use href="#eye"/></svg></span><svg class="layer__chevron"><use href="#chev-down"/></svg><svg class="layer__folder"><use href="#folder"/></svg><span class="layer__name">ALPINE RIDGE TRAVERSE</span></div>
    <div class="layer layer--group layer--child layer--active"><span class="layer__eye"><svg><use href="#eye"/></svg></span><svg class="layer__chevron"><use href="#chev-right"/></svg><svg class="layer__folder"><use href="#folder"/></svg><span class="layer__name">Distance Dial</span></div>
    <div class="layer layer--group layer--child"><span class="layer__eye"><svg><use href="#eye"/></svg></span><svg class="layer__chevron"><use href="#chev-right"/></svg><svg class="layer__folder"><use href="#folder"/></svg><span class="layer__name">STATISTICS SECTION</span></div>
    <div class="layer layer--group layer--child"><span class="layer__eye"><svg><use href="#eye"/></svg></span><svg class="layer__chevron"><use href="#chev-right"/></svg><svg class="layer__folder"><use href="#folder"/></svg><span class="layer__name">OPTIONAL EVENT PHOTO</span></div>
    <div class="layer layer--group layer--child"><span class="layer__eye"><svg><use href="#eye"/></svg></span><svg class="layer__chevron"><use href="#chev-right"/></svg><svg class="layer__folder"><use href="#folder"/></svg><span class="layer__name">Pace Legend</span></div>
    <div class="layer layer--group layer--child"><span class="layer__eye"><svg><use href="#eye"/></svg></span><svg class="layer__chevron"><use href="#chev-right"/></svg><svg class="layer__folder"><use href="#folder"/></svg><span class="layer__name">ELEVATION PROFILE</span></div>

    <div class="layer layer--item layer--text"><span class="layer__eye"><svg><use href="#eye"/></svg></span><span class="type-icon">T</span><span class="layer__name">kelvoadventure.com</span></div>
    <div class="layer layer--item"><span class="layer__eye"><svg><use href="#eye"/></svg></span><span class="thumb"></span><span class="layer__name">kelvo-logo-g12</span></div>
    <div class="layer layer--item layer--text"><span class="layer__eye"><svg><use href="#eye"/></svg></span><span class="type-icon">T</span><span class="layer__name">ALPINE RIDGE</span></div>
    <div class="layer layer--item layer--text"><span class="layer__eye"><svg><use href="#eye"/></svg></span><span class="type-icon">T</span><span class="layer__name">LOCATION</span></div>
    <div class="layer layer--item layer--text"><span class="layer__eye"><svg><use href="#eye"/></svg></span><span class="type-icon">T</span><span class="layer__name">TRAIL RUNNING</span></div>
    <div class="layer layer--item layer--text"><span class="layer__eye"><svg><use href="#eye"/></svg></span><span class="type-icon">T</span><span class="layer__name">ACTIVITY</span></div>
    <div class="layer layer--item layer--text"><span class="layer__eye"><svg><use href="#eye"/></svg></span><span class="type-icon">T</span><span class="layer__name">12 OCTOBER 2025</span></div>
    <div class="layer layer--item layer--text"><span class="layer__eye"><svg><use href="#eye"/></svg></span><span class="type-icon">T</span><span class="layer__name">15 KM | L...OZER LINE</span></div>
    <div class="layer layer--item layer--text"><span class="layer__eye"><svg><use href="#eye"/></svg></span><span class="type-icon">T</span><span class="layer__name">RHEN DALLOW</span></div>
    <div class="layer layer--item layer--text"><span class="layer__eye"><svg><use href="#eye"/></svg></span><span class="type-icon">T</span><span class="layer__name">ALPINE RI... TRAVERSE</span></div>

    <div class="layer layer--item"><span class="layer__eye"><svg><use href="#eye"/></svg></span><span class="thumb"></span><span class="layer__name">&lt;Path&gt;</span></div>
    <div class="layer layer--item"><span class="layer__eye"><svg><use href="#eye"/></svg></span><span class="thumb"></span><span class="layer__name">&lt;Path&gt;</span></div>
    <div class="layer layer--item"><span class="layer__eye"><svg><use href="#eye"/></svg></span><span class="thumb"></span><span class="layer__name">&lt;Path&gt;</span></div>
    <div class="layer layer--item"><span class="layer__eye"><svg><use href="#eye"/></svg></span><span class="thumb"></span><span class="layer__name">&lt;Path&gt;</span></div>
    <div class="layer layer--item"><span class="layer__eye"><svg><use href="#eye"/></svg></span><span class="thumb thumb--mark"></span><span class="layer__name">&lt;Path&gt;</span></div>
    <div class="layer layer--item"><span class="layer__eye"><svg><use href="#eye"/></svg></span><span class="thumb thumb--dark"></span><svg class="link-icon"><use href="#link"/></svg><span class="mask-thumb"></span><span class="layer__name">&lt;Clip Group&gt;</span></div>
    <div class="layer layer--item"><span class="layer__eye"><svg><use href="#eye"/></svg></span><span class="thumb" style="margin-left:20px"></span><span class="layer__name">MAP COLOUR GRADE</span></div>
    <div class="layer layer--item"><span class="layer__eye"><svg><use href="#eye"/></svg></span><span class="thumb thumb--map" style="margin-left:20px"></span><span class="layer__name">&lt;Image&gt;</span></div>
  </div>

  <div class="scrollbar"><div class="scrollbar__thumb"></div></div>
</section>

<div class="panel-edge"></div>
</body>
</html>
```